Podcast Cover Art for Fast Growing Show (Ill include a gracious tip!)

This artwork is for "The Steadfast Fellow Show." The podcast is for men, and it's all about self-improvement, confidence, success, money, women and masculinity. It's for the guy who wants to improve himself. I'd like for my picture to be included — in black and white — and I want the text to read: "The Steadfast Fellow Show" and somewhere in there it'll say: "with Dale Prowen." I'm open to color schemes. The podcast is a little edgy so I'd like for that to be represented in the design. Thank you! (((Here's the podcast page if you wanna check it out: http://steadfastfellowshow.castorbit.net/)))

Target Market(s)

Men who want to attract women and improve their lives!

Font styles to use
Serif

Colors

Designer to choose colors to be used in the design.

Requirements
Must have
• My image in it (in black and white) and the two titles: "The Steadfast Fellow Show" and "with Dale Prowen"
Nice to have
• My logo in it somehow (which is the arrow looking logo attached below). I've also found that my image looks best in black and white and with a circular type cut out (although I'm open to different design ideas). I've attached my logo with a circular cut out below so you can see what I'm talking about.
Should not have
• Flowers. Teddy bears. ice cream.

```html
<!DOCTYPE html>
<html lang="en">
<head>
<meta charset="utf-8">
<title>The Steadfast Fellow Show — Cover Art</title>
<link rel="stylesheet" href="https://fonts.googleapis.com/css2?family=Anton&family=Montserrat:wght@300;400&family=Questrial&display=swap">
<style>
  :root {
    --stage-blue: #2f4a9c;
    --stage-violet: #4a2f72;
    --stage-red: #6a2550;
    --stage-sky: #3f78b8;
    --cover-black: #050506;
    --title-white: #f4f4f4;
    --accent-red: #c0121c;
    --label-grey: #b9b9b9;
    --tag-box: #3a3a3c;
    --glow-red: #6e0f1e;
    --glow-blue: #13225e;
    --portrait-light: #5a5a5c;
    --portrait-dark: #121213;
    --caption: #ffffff;
  }
  * { margin: 0; padding: 0; box-sizing: border-box; }
  html, body {
    width: 1200px;
    height: 1058px;
    overflow: hidden;
  }
  body {
    background:
      radial-gradient(ellipse 40% 45% at 0% 50%, var(--stage-red), transparent 70%),
      radial-gradient(ellipse 45% 40% at 100% 40%, var(--stage-sky), transparent 70%),
      radial-gradient(ellipse 40% 30% at 85% 0%, #6a6aa8, transparent 70%),
      linear-gradient(160deg, var(--stage-blue) 0%, var(--stage-violet) 50%, #24348f 100%);
  }
  .stage {
    position: relative;
    width: 1200px;
    height: 1058px;
  }
  .cover {
    position: absolute;
    left: 217px;
    top: 110px;
    width: 772px;
    height: 772px;
    display: block;
    box-shadow: 0 10px 40px rgba(0, 0, 0, 0.35);
  }
  .title-small {
    font-family: "Montserrat", sans-serif;
    font-weight: 300;
    fill: var(--accent-red);
  }
  .title-main {
    font-family: "Anton", sans-serif;
    fill: var(--title-white);
  }
  .tag-text {
    font-family: "Montserrat", sans-serif;
    font-weight: 400;
    fill: var(--label-grey);
  }
  .brand-name {
    font-family: "Montserrat", sans-serif;
    font-weight: 400;
    fill: var(--title-white);
  }
  .host-line {
    font-family: "Montserrat", sans-serif;
    font-weight: 400;
  }
  .host-with { fill: var(--label-grey); }
  .host-name { fill: var(--accent-red); }
  .caption {
    position: absolute;
    left: 0;
    top: 932px;
    width: 1200px;
    text-align: center;
    font-family: "Questrial", sans-serif;
    font-size: 27px;
    line-height: 35px;
    color: var(--caption);
    letter-spacing: 0.2px;
  }
</style>
</head>
<body>
<main class="stage">
  <svg class="cover" viewBox="0 0 772 772" xmlns="http://www.w3.org/2000/svg">
    <defs>
      <radialGradient id="glowRed" cx="0.9" cy="0.62" r="0.4">
        <stop offset="0" stop-color="var(--glow-red)" stop-opacity="0.9"/>
        <stop offset="1" stop-color="var(--glow-red)" stop-opacity="0"/>
      </radialGradient>
      <radialGradient id="glowBlue" cx="0.08" cy="0.72" r="0.35">
        <stop offset="0" stop-color="var(--glow-blue)" stop-opacity="0.9"/>
        <stop offset="1" stop-color="var(--glow-blue)" stop-opacity="0"/>
      </radialGradient>
      <radialGradient id="portraitTone" cx="0.5" cy="0.35" r="0.6">
        <stop offset="0" stop-color="var(--portrait-light)"/>
        <stop offset="0.6" stop-color="#2a2a2b"/>
        <stop offset="1" stop-color="var(--portrait-dark)" stop-opacity="0"/>
      </radialGradient>
      <filter id="distressed" x="0" y="0" width="100%" height="100%">
        <feTurbulence type="fractalNoise" baseFrequency="0.35 0.06" numOctaves="3" seed="7" result="noise"/>
        <feColorMatrix in="noise" type="matrix"
          values="0 0 0 0 0  0 0 0 0 0  0 0 0 0 0  2.6 0 0 0 -1.1" result="spots"/>
        <feComponentTransfer in="spots" result="holes">
          <feFuncA type="discrete" tableValues="0 0 0 0 0 1"/>
        </feComponentTransfer>
        <feComposite in="SourceGraphic" in2="holes" operator="out"/>
      </filter>
    </defs>

    <rect class="cover-base" width="772" height="772" fill="var(--cover-black)"/>
    <rect class="cover-glow-red" width="772" height="772" fill="url(#glowRed)"/>
    <rect class="cover-glow-blue" width="772" height="772" fill="url(#glowBlue)"/>

    <rect class="host-portrait" x="90" y="45" width="640" height="540" fill="url(#portraitTone)"
          role="img" aria-label="Black and white portrait of host Dale Prowen, hands steepled in front of his chin"/>

    <text class="title-small" x="45" y="456" font-size="42" textLength="113" lengthAdjust="spacingAndGlyphs">THE</text>
    <text class="title-main" x="45" y="594" font-size="150" textLength="676" lengthAdjust="spacingAndGlyphs" filter="url(#distressed)">STEADFAST</text>
    <text class="title-small" x="498" y="646" font-size="55" textLength="218" lengthAdjust="spacingAndGlyphs">FELLOW</text>

    <rect class="tag-box" x="531" y="659" width="185" height="21" fill="var(--tag-box)"/>
    <text class="tag-text" x="623.5" y="675" font-size="15" text-anchor="middle" letter-spacing="14">SHOW</text>

    <g class="brand-mark">
      <rect x="352" y="655" width="9" height="9" fill="var(--title-white)"/>
      <text class="brand-name" x="366" y="664" font-size="11" letter-spacing="1">STEADFAST</text>
    </g>

    <text class="host-line" x="168" y="732" font-size="20" textLength="443" lengthAdjust="spacing"><tspan class="host-with">WITH </tspan><tspan class="host-name">DALE PROWEN</tspan></text>
  </svg>

  <p class="caption">PODCAST COVER ART FOR FAST GROWING<br>SHOW (ILL INCLUDE A GRACIOUS TIP!)</p>
</main>
</body>
</html>
```